QuillMark Business Cards

I need a business card designed for QuillMark. To get an idea of what we do please visit https://formvault.example/para-creadores-3

```html
<!DOCTYPE html>
<html lang="en">
<head>
<meta charset="UTF-8">
<title>QuillMark Business Cards</title>
<link rel="stylesheet" href="https://fonts.googleapis.com/css2?family=Montserrat:wght@300;400&family=Poppins:wght@300;600;700&display=swap">
<style>
  :root {
    --paper: #e8e8e8;
    --card-dark: #1c1e23;
    --card-dark-soft: #23252b;
    --pattern-tone: #2c2a27;
    --accent: #f0961e;
    --ink-light: #ffffff;
  }
  * { box-sizing: border-box; margin: 0; padding: 0; }
  html, body {
    width: 1200px;
    height: 1200px;
    overflow: hidden;
    background: var(--paper);
  }
  .sheet {
    width: 1200px;
    height: 1200px;
    display: flex;
    flex-direction: column;
    align-items: center;
    justify-content: center;
    gap: 60px;
  }
  .card {
    position: relative;
    width: 840px;
    height: 480px;
    overflow: hidden;
    background: var(--card-dark);
    box-shadow: 0 10px 28px rgba(0,0,0,0.18);
  }

  /* Front face */
  .front-top {
    position: absolute;
    inset: 0 0 160px 0;
    background: radial-gradient(ellipse at center, var(--pattern-tone) 0%, var(--card-dark) 75%);
  }
  .front-brand {
    position: absolute;
    left: 0; right: 0;
    top: 140px;
    text-align: center;
    font-family: "Montserrat", sans-serif;
    font-weight: 300;
    font-size: 38px;
    letter-spacing: 0.18em;
    color: var(--ink-light);
  }
  .front-band {
    position: absolute;
    left: 0; right: 0; bottom: 0;
    height: 160px;
    background: var(--accent);
    display: flex;
    align-items: center;
    justify-content: center;
  }
  .front-tagline {
    font-family: "Montserrat", sans-serif;
    font-weight: 400;
    font-size: 19px;
    letter-spacing: 0.3em;
    color: var(--ink-light);
  }

  /* Back face */
  .back-brand {
    position: absolute;
    left: 70px;
    top: 60px;
    font-family: "Montserrat", sans-serif;
    font-weight: 400;
    font-size: 24px;
    letter-spacing: 0.16em;
    color: var(--accent);
  }
  .back-person {
    position: absolute;
    left: 150px;
    top: 195px;
    width: 240px;
    text-align: center;
    color: var(--ink-light);
    font-family: "Poppins", sans-serif;
  }
  .person-name {
    font-weight: 300;
    font-size: 38px;
    line-height: 1.1;
  }
  .person-role {
    font-weight: 700;
    font-size: 38px;
    line-height: 1.1;
  }
  .back-divider {
    position: absolute;
    left: 430px;
    top: 95px;
    width: 4px;
    height: 300px;
    background: var(--accent);
  }
  .contact-list {
    position: absolute;
    left: 475px;
    top: 140px;
    list-style: none;
    display: flex;
    flex-direction: column;
    gap: 30px;
  }
  .contact-item {
    display: flex;
    align-items: center;
    gap: 18px;
    font-family: "Poppins", sans-serif;
    font-weight: 600;
    font-size: 18px;
    color: var(--accent);
  }
  .contact-icon {
    width: 26px;
    height: 26px;
    flex: none;
    fill: none;
    stroke: var(--accent);
    stroke-width: 1.6;
    stroke-linecap: round;
    stroke-linejoin: round;
  }
</style>
</head>
<body>
<main class="sheet">

  <section class="card card-front">
    <div class="front-top" role="img" aria-label="Faint geometric line pattern in dark bronze tones"></div>
    <div class="front-brand">QUILLMARK</div>
    <div class="front-band">
      <p class="front-tagline">DIGITAL NOTARY</p>
    </div>
  </section>

  <section class="card card-back">
    <div class="back-brand">QUILLMARK</div>

    <div class="back-person">
      <p class="person-name">NAME</p>
      <p class="person-role">CEO</p>
    </div>

    <div class="back-divider"></div>

    <ul class="contact-list">
      <li class="contact-item">
        <svg class="contact-icon" viewBox="0 0 26 26" aria-hidden="true">
          <rect x="3" y="6" width="20" height="14"/>
          <path d="M3 6l10 8 10-8"/>
        </svg>
        <span>EMAIL</span>
      </li>
      <li class="contact-item">
        <svg class="contact-icon" viewBox="0 0 26 26" aria-hidden="true">
          <circle cx="13" cy="13" r="10"/>
          <ellipse cx="13" cy="13" rx="4.5" ry="10"/>
          <path d="M3 13h20M5 8h16M5 18h16"/>
        </svg>
        <span>COMPANY.COM</span>
      </li>
      <li class="contact-item">
        <svg class="contact-icon" viewBox="0 0 26 26" aria-hidden="true">
          <path d="M13 24s-7-8-7-13a7 7 0 0 1 14 0c0 5-7 13-7 13z"/>
          <circle cx="13" cy="11" r="2.5"/>
        </svg>
        <span>ADDRESS</span>
      </li>
      <li class="contact-item">
        <svg class="contact-icon" viewBox="0 0 26 26" aria-hidden="true">
          <rect x="7" y="2" width="12" height="22" rx="2"/>
          <path d="M11 20h4"/>
        </svg>
        <span>PHONE NUMBER</span>
      </li>
    </ul>
  </section>

</main>
</body>
</html>
```